Systems and Technology Consultants - Website

Design & Build a website for a new company which operates in the Systems and Technology space for Transportation, Government and Commercial sectors.

Overall design should be minimalist in nature.
Should also have a feed that provides news and event updates on the main page.
Logo has already been awarded and should be incorporated into the site.

We like the overall layout, functionality and simplicity of the below sites. Submitted designs could be similar to or a combination of the aspects on these sites, or perhaps a whole different concept - we are open to new ideas.
Vortrane.com
Merp.it

Update 1 Dated 27 May 2014

All I am moving away from the Merp.it website and would like it to be more aligned with Vortrane.com not only in layout but in functionality. I will be extending the deadline of this design brief for two weeks to incorporate additional requirements and will add addtional funding to the project.

Apologies for not having more information available to provide but with so many submissions its getting confusing.

Thanks Dermot
Updates

Please note that the brief has been updated and the deadline has been extended.

Important: We will need two language versions of the website, English and Arabic; the website is hosted on HostPeak

Hello All, Thank you for your submissions. We have narrowed it down to the final 6 designers and I just wanted to take a moment and provide a bit of feedback regarding the concepts that we like and the modifications we are looking for. First, let me mention some of the design functions we like. - At the top of the homepage we really like the "region" or "language" tab so that the website can be viewed in both English and Arabic. - We like the homepage to have clear color variation so that the different sections of the homepage are distinct. Additionally, we like the bottom portion of the homepage to be in red. We feel that draws attention to our contact information. Again, we would like the colors to integrate black, gray-scale, red, etc. - Having a search tab at the top of the home page, or integrated into the main image, so that the site is easy to navigate. - We especially like the main image to have the scrolling tabs at the bottom so it is easy to browse the services offered (Consultancy, Solutions Architecture, Masters Systems Integration, Independent Design Review). - In regards to the services offered tab we really like the idea that a few people presented that have the outside of our logo with an icon in the middle of consultancy, solutions, etc., etc. Secondly, as mentioned in our brief we really enjoy the design of vortrane site. Specially, we enjoy the strong iconic images they use, the way the tabs at the top scroll easily, and contact us page that generates an email. Lastly, I've included some photos of the concept we have been working on. What we are trying to demonstrate is how our company offers a range of services that are essentially linked together. We provide individual services that when combined present the full service package. We would like this concept to be integrated into the over concept of our website. Please feel free to ask for clarification of any of the above points or contact us if you have any additional questions. We appreciate all of your hard work and are very excited to see the updated designs. Best, Miriam Dowbrook Plenvaro Senior Program Manager miriam.dowbrook@plenvaro-mail.com

Industry/Entity Type

Government

Font styles to use
Serif
Sans Serif

Requirements
Must have
• Must work on/adapt to various/mobile devices (responsive)
Must be simple and straightforward
Colors should be in line/matching with logo
2 language versions: English and Arabic (no Thai)
Services should be the first group/row of items after/below the main image
Note: the website will be hosted by hostpeak
Nice to have
• Submit feedback form
What's New section
The banner at the bottom of the site should not be too large; we would like a narrow one more
It would be nice if the header/top banner (with Home, About, etc. tabs) could stay in place as you scroll down (like Vortrane and Chatterly)
We will likely only use one image with a Company slogan on the Home page rather than a carousel of images to rotate through
Should not have
• This is the existing website: http://www.plenvaro-example.org
We do not like the animation, the way the banner icons/titles bounce
Not simple enough, we don't like the functionality or how pages load so slowly
We do not like the logo centered - it should be at the left
The banner and its tabs should not be towards the right, we would like them to be centered, to go all the way across and to be below the logo

```html
<!DOCTYPE html>
<html lang="en">
<head>
<meta charset="utf-8">
<title>Plenvaro — System Knowledge Delivered</title>
<link rel="stylesheet" href="https://fonts.googleapis.com/css2?family=Roboto:wght@300;400;500&display=swap">
<style>
:root{
  --red:#e8313c;
  --red-dark:#e01f2a;
  --ink:#222;
  --header:#2b2b2b;
  --panel:#3a3a3a;
  --light:#f1f1f1;
  --band:#e4e4e4;
  --grey:#8a8a8a;
  --text:#6b6b6b;
  --white:#fff;
}
*{box-sizing:border-box;margin:0;padding:0}
html,body{width:686px;height:1200px;overflow:hidden}
body{font-family:'Roboto',Arial,sans-serif;background:var(--light);position:relative;color:var(--ink)}
.abs{position:absolute}

/* header */
.site-header{left:0;top:0;width:686px;height:78px;background:linear-gradient(#303030,#252525)}
.region-select{right:42px;top:0;width:58px;height:17px;background:#454545;color:#bbb;font-size:6px;line-height:17px;text-align:center}
.main-nav a{position:absolute;top:46px;color:var(--white);font-size:8px;font-weight:500;text-decoration:none;letter-spacing:.2px}
.brand{left:293px;top:14px;width:100px;text-align:center}
.brand-mark{display:block;margin:0 auto 6px;width:26px;height:26px;border:2px solid var(--red);border-radius:50%}
.brand-name{color:var(--red);font-size:8px;font-weight:500;letter-spacing:2px}

/* hero */
.hero{left:0;top:78px;width:686px;height:291px;background:radial-gradient(ellipse at 55% 45%,#2f5d6b 0%,#1b2f3a 45%,#0f1820 100%)}
.hero-title{left:163px;top:191px;width:360px;height:64px;background:rgba(20,20,20,.55);text-align:center}
.hero-title h1{color:var(--red);font-weight:400;font-size:32px;line-height:34px;margin-top:2px}
.hero-title p{color:var(--white);font-size:20px;line-height:24px;letter-spacing:.3px}

/* welcome */
.welcome{left:0;top:369px;width:686px;height:170px;background:var(--light)}
.rule{height:1px;background:#cfcfcf}
.section-title{color:var(--red);font-weight:300;font-size:20px;text-align:center;letter-spacing:.3px}
.welcome-text{left:90px;width:506px;top:72px;color:var(--grey);font-weight:300;font-size:15px;line-height:20px;text-align:center}

/* services */
.services{left:0;top:539px;width:686px;height:216px;background:var(--band)}
.service{width:110px;text-align:center}
.service svg{display:block;margin:0 auto}
.service h3{margin-top:12px;font-weight:400;font-size:11px;color:#444;letter-spacing:.3px}
.service.active h3{color:var(--red)}
.btn-more{display:inline-block;margin-top:8px;width:46px;height:16px;line-height:16px;font-size:7px;color:var(--white);background:var(--grey)}
.service.active .btn-more{background:var(--red-dark)}

/* news */
.news-title{left:42px;top:780px;color:var(--red);font-weight:300;font-size:21px}
.news-item{left:42px;width:377px}
.news-thumb{position:absolute;left:0;top:0;width:110px;height:75px}
.news-body{position:absolute;left:122px;top:0;width:255px}
.news-body h4{font-weight:400;font-size:10px;line-height:13px;color:#222}
.news-body p{margin-top:5px;font-size:6.6px;line-height:13px;color:var(--text)}
.news-body a{color:var(--red);text-decoration:none}
.btn-read-all{left:42px;top:1028px;width:76px;height:22px;background:#666;color:var(--white);font-size:10px;line-height:22px;text-align:center}

/* feedback */
.feedback{left:454px;top:755px;width:190px;height:314px;background:var(--panel)}
.feedback h2{position:absolute;left:12px;top:26px;color:var(--white);font-weight:300;font-size:19px}
.feedback label{position:absolute;left:12px;color:var(--white);font-size:7.5px}
.field{position:absolute;left:12px;width:164px;height:18px;background:var(--white)}
.btn-submit{position:absolute;left:101px;top:264px;width:75px;height:23px;background:var(--red-dark);color:var(--white);font-size:9.5px;line-height:23px;text-align:center}

/* footer */
.site-footer{left:0;top:1069px;width:686px;height:131px;background:linear-gradient(#ef4350,#e71e2b)}
.foot-col{top:18px}
.foot-col h5{font-weight:400;font-size:8.5px;color:#3a0a0d;margin-bottom:4px}
.foot-col li{list-style:none;font-size:7.5px;line-height:14.3px;color:var(--white)}
.foot-contact li{display:flex;align-items:center;gap:8px;line-height:18px}
.social li{display:flex;align-items:center;gap:7px;line-height:18.5px}
.dot{width:11px;height:11px;border-radius:50%;background:var(--white);flex:none}
.foot-brand{left:508px;top:18px;width:100px;text-align:center;color:var(--white)}
.foot-brand .brand-mark{border-color:var(--white);width:30px;height:30px}
.foot-brand .brand-name{color:var(--white);font-size:8px}
.copyright{left:524px;top:1157px;color:var(--white);font-size:7px}
</style>
</head>
<body>

<header class="site-header abs">
  <div class="region-select abs">Select Region</div>
  <nav class="main-nav">
    <a style="left:42px">HOME</a>
    <a style="left:105px">BUSINESS UNIT</a>
    <a style="left:204px">SERVICES</a>
    <a style="left:433px">ABOUT US</a>
    <a style="left:512px">LOCATIONS</a>
    <a style="left:595px">CONTACT US</a>
  </nav>
  <div class="brand abs"><span class="brand-mark"></span><span class="brand-name">PLENVARO</span></div>
</header>

<section class="hero abs" role="img" aria-label="Businessman in a suit touching a glowing network of connected nodes"></section>
<div class="hero-title abs"><h1>PLENVARO</h1><p>SYSTEM KNOWLEDGE DELIVERED</p></div>

<section class="welcome abs">
  <div class="rule abs" style="left:42px;top:38px;width:150px"></div>
  <div class="rule abs" style="left:494px;top:38px;width:150px"></div>
  <h2 class="section-title abs" style="left:0;width:686px;top:27px">WELCOME TO PLENVARO</h2>
  <p class="welcome-text abs">PLENVARO SPECIALIZES IN DELIVERING QUALITY PROFESSIONAL SERVICES AND TECHNICAL PROJECTS THAT SUPPORT LARGER BUSINESS GOALS.</p>
</section>

<section class="services abs">
  <h2 class="section-title abs" style="left:0;width:686px;top:26px">SERVICES WE OFFERED</h2>

  <div class="service active abs" style="left:41px;top:78px">
    <svg width="60" height="48" viewBox="0 0 60 48"><ellipse cx="32" cy="19" rx="26" ry="17" fill="#222"/><path d="M10 27 L4 44 L20 33Z" fill="#222"/><circle cx="22" cy="19" r="3.5" fill="#fff"/><circle cx="32" cy="19" r="3.5" fill="#fff"/><circle cx="42" cy="19" r="3.5" fill="#fff"/></svg>
    <h3>CONSULTING</h3><span class="btn-more">read more</span>
  </div>

  <div class="service abs" style="left:165px;top:78px">
    <svg width="60" height="48" viewBox="0 0 60 48" fill="none" stroke="#777" stroke-width="3"><path d="M14 4 V44"/><path d="M14 12 L44 42 H14"/><rect x="22" y="20" width="28" height="14"/></svg>
    <h3>ENGINEERING</h3><span class="btn-more">read more</span>
  </div>

  <div class="service abs" style="left:288px;top:78px">
    <svg width="60" height="48" viewBox="0 0 60 48" fill="#777"><path d="M27 2 H33 L43 42 H17Z"/><rect x="12" y="42" width="36" height="5"/><rect x="23" y="14" width="14" height="5" fill="#e4e4e4"/><rect x="20" y="26" width="20" height="5" fill="#e4e4e4"/></svg>
    <h3>CONSTRUCTION</h3><span class="btn-more">read more</span>
  </div>

  <div class="service abs" style="left:412px;top:78px">
    <svg width="66" height="48" viewBox="0 0 66 48"><circle cx="22" cy="28" r="16" fill="none" stroke="#777" stroke-width="7" stroke-dasharray="5 3.4"/><circle cx="22" cy="28" r="10" fill="#777"/><circle cx="22" cy="28" r="4" fill="#e4e4e4"/><circle cx="48" cy="13" r="10" fill="none" stroke="#777" stroke-width="5" stroke-dasharray="4 2.3"/><circle cx="48" cy="13" r="6" fill="#777"/><circle cx="48" cy="13" r="2.5" fill="#e4e4e4"/></svg>
    <h3>OPERATIONS</h3><span class="btn-more">read more</span>
  </div>

  <div class="service abs" style="left:535px;top:78px">
    <svg width="60" height="48" viewBox="0 0 60 48" stroke="#777" stroke-linecap="round" fill="none"><path d="M18 8 L46 42" stroke-width="7"/><circle cx="16" cy="8" r="7" stroke-width="4"/><path d="M46 6 L16 42" stroke-width="6"/><path d="M44 4 L50 10" stroke-width="8"/></svg>
    <h3>MAINTENANCE</h3><span class="btn-more">read more</span>
  </div>
</section>

<h2 class="news-title abs">WHAT'S NEW</h2>

<article class="news-item abs" style="top:820px;height:75px">
  <div class="news-thumb" role="img" aria-label="Businessman touching a glowing interface with gears" style="background:linear-gradient(135deg,#6f6f6f,#c9b48a 55%,#3d3d3d)"></div>
  <div class="news-body">
    <h4>DUIS ALIQUAM NIBH A DUI IACULIS VIVERRA ID A VELIT. VIVAMUS EGESTAS RISUS IN MAGNA VARIUS..</h4>
    <p>Aenean a nibh eget turpis vehicula tempus ac sed massa. Vestibulum dolor nulla, ultrices ac tincidunt sed, laoreet non est. Suspendisse lobortis turpis in odio blandit ac interdum lorem euismod. Etiam risus massa, vulputate eu pellentesque et, consectetur a neque...<a>Continue Reading</a></p>
  </div>
</article>
<div class="rule abs" style="left:42px;top:910px;width:377px"></div>
<article class="news-item abs" style="top:923px;height:75px">
  <div class="news-thumb" role="img" aria-label="Network cables plugged into a server switch" style="background:linear-gradient(135deg,#2f4a3a,#6b8c5a 45%,#1e2a2a)"></div>
  <div class="news-body">
    <h4>DUIS ALIQUAM NIBH A DUI IACULIS VIVERRA ID A VELIT. VIVAMUS EGESTAS RISUS IN MAGNA VARIUS..</h4>
    <p>Aenean a nibh eget turpis vehicula tempus ac sed massa. Vestibulum dolor nulla, ultrices ac tincidunt sed, laoreet non est. Suspendisse lobortis turpis in odio blandit ac interdum lorem euismod. Etiam risus massa, vulputate eu pellentesque et, consectetur a neque...<a>Continue Reading</a></p>
  </div>
</article>
<div class="btn-read-all abs">READ ALL</div>

<aside class="feedback abs">
  <h2>FEEDBACK</h2>
  <label style="top:60px">NAME</label><div class="field" style="top:71px"></div>
  <label style="top:104px">EMAIL ADDRESS</label><div class="field" style="top:114px"></div>
  <label style="top:146px">CONTACT NO.</label><div class="field" style="top:156px"></div>
  <label style="top:190px">MESSAGE.</label><div class="field" style="top:200px;height:56px"></div>
  <div class="btn-submit">SUBMIT NOW</div>
</aside>

<footer class="site-footer abs">
  <div class="foot-col abs" style="left:42px"><h5>COMPANY</h5><ul><li>Home</li><li>Business Units</li><li>Services</li><li>About Us</li><li>Locations</li><li>Contact Us</li></ul></div>
  <div class="foot-col abs" style="left:151px"><h5>SERVICES</h5><ul><li>Consulting</li><li>Engineering</li><li>Construction</li><li>Operations</li><li>Maintenance</li></ul></div>
  <div class="foot-col foot-contact abs" style="left:249px"><h5>CONTACT INFO</h5><ul>
    <li>We want to hear from you:</li>
    <li><svg width="11" height="9" viewBox="0 0 11 9" fill="#fff"><path d="M1 3 Q5.5 -1 10 3 L8 4 L7 2.5 H4 L3 4Z"/><rect x="2" y="5" width="7" height="4" rx="1"/></svg>+(00)-02-555-0142-9</li>
    <li><svg width="11" height="8" viewBox="0 0 11 8"><rect x=".5" y=".5" width="10" height="7" fill="none" stroke="#fff"/><path d="M.5 .5 L5.5 4.5 L10.5 .5" fill="none" stroke="#fff"/></svg>info@plenvaro-example.org</li>
  </ul></div>
  <div class="foot-col social abs" style="left:394px"><h5>CONNECT US</h5><ul>
    <li><span class="dot"></span>Chatterly</li><li><span class="dot"></span>Chirpnet</li><li><span class="dot"></span>Linkpro</li><li><span class="dot"></span>Rss</li>
  </ul></div>
  <div class="foot-brand abs"><span class="brand-mark"></span><span class="brand-name">PLENVARO</span></div>
</footer>
<div class="copyright abs">Copyright © 2014. All Right Reserved</div>

</body>
</html>
```